Tranquil Pathway Business Card

Logo attached. (will be printing onto thick white/off white textured card)

Double sided business card for two Therapists working at Tranquil Pathway.

Require one design, but with different name and mobile numbers on each card.

Target Market(s)

Medical, Health

Industry/Entity Type

Business

Contact Information for Business Card

Need one business card design, but a separate card for each person - Colin Marchetti and Marieke de Boeckx.

FRONT OF CARD

Logo

Name (Colin Marchetti on one card, Marieke de Boeckx on the other)
Professional Clinical Hypnotherapist

Consulting Rooms (Near Lindqvist Hospital)
482 Brackenfield Road
Dunmore VIC 3987

Colin@TranquilPathway.example.au OR Marieke@TranquilPathway.example.au

Mobile: 0455 872 604 (for Colin) OR
Mobile: 0467 290 518 (for Marieke)

BACK OF CARD

Logo

Website: www.TranquilPathway.example.au

Phone: 1300 958 471

Requirements
Must have
• Text and logo only. No additiional graphics.

```html
<!DOCTYPE html>
<html lang="en">
<head>
<meta charset="utf-8">
<title>Tranquil Pathway Business Card</title>
<link rel="stylesheet" href="https://fonts.googleapis.com/css2?family=Ubuntu:wght@400;500;700&display=swap">
<style>
  :root {
    --backdrop: #cccccc;
    --card: #ffffff;
    --navy: #222a5e;
    --slate: #666666;
    --ink: #111111;
  }
  * { margin: 0; padding: 0; box-sizing: border-box; }
  html, body { width: 1200px; height: 1000px; overflow: hidden; }
  body {
    background: var(--backdrop);
    font-family: "Ubuntu", sans-serif;
    color: var(--ink);
    position: relative;
  }
  .card {
    position: absolute;
    background: var(--card);
  }
  .card--front { left: 227px; top: 66px; width: 746px; height: 432px; }
  .card--back  { left: 226px; top: 509px; width: 747px; height: 425px; }

  .brand { position: absolute; display: flex; align-items: center; }
  .brand__mark { display: block; }
  .brand__divider { width: 3px; background: var(--slate); }
  .brand__name {
    font-family: "Ubuntu", sans-serif;
    font-weight: 500;
    color: var(--navy);
    text-transform: uppercase;
    line-height: 1.02;
    letter-spacing: 1px;
  }

  .card--front .brand { left: 156px; top: 50px; }
  .card--front .brand__mark { width: 142px; height: 142px; }
  .card--front .brand__divider { height: 130px; margin: 0 17px 0 7px; }
  .card--front .brand__name { font-size: 36px; }

  .card--back .brand { left: 140px; top: 108px; }
  .card--back .brand__mark { width: 150px; height: 150px; }
  .card--back .brand__divider { height: 140px; margin: 0 18px 0 11px; }
  .card--back .brand__name { font-size: 38px; }

  .person { position: absolute; left: 98px; top: 215px; width: 200px; text-align: center; }
  .person__name { font-size: 19px; font-weight: 700; line-height: 1.2; }
  .person__role { font-size: 10.5px; margin-top: 3px; }

  .address { position: absolute; left: 344px; top: 268px; font-size: 17px; line-height: 21.5px; }

  .contact { position: absolute; left: 105px; top: 351px; font-size: 11px; }
  .contact p + p { margin-top: 14px; }

  .footer-rule {
    position: absolute; left: 41px; top: 368px; width: 665px; height: 5px;
    background: var(--navy);
  }
  .footer-line {
    position: absolute; left: 41px; top: 382px; width: 665px;
    display: flex; justify-content: space-between;
    font-size: 19.5px; white-space: nowrap;
  }
</style>
</head>
<body>

<section class="card card--front">
  <div class="brand">
    <svg class="brand__mark" viewBox="0 0 142 142" aria-hidden="true">
      <circle cx="71" cy="71" r="62" fill="var(--navy)"/>
    </svg>
    <span class="brand__divider"></span>
    <span class="brand__name">Tranquil<br>Pathway</span>
  </div>

  <div class="person">
    <p class="person__name">Marieke de Boeckx</p>
    <p class="person__role">Professional Clinical Hypnotherapist</p>
  </div>

  <address class="address" style="font-style:normal">
    Consulting Rooms (Near Lindqvist Hospital)<br>
    482 Brackenfield Road<br>
    Dunmore VIC 3987
  </address>

  <div class="contact">
    <p>Marieke@TranquilPathway.example.au</p>
    <p>Mobile: 0467 290 518</p>
  </div>
</section>

<section class="card card--back">
  <div class="brand">
    <svg class="brand__mark" viewBox="0 0 150 150" aria-hidden="true">
      <circle cx="75" cy="75" r="66" fill="var(--navy)"/>
    </svg>
    <span class="brand__divider"></span>
    <span class="brand__name">Tranquil<br>Pathway</span>
  </div>

  <div class="footer-rule"></div>
  <div class="footer-line">
    <span>Website: www.TranquilPathway.example.au</span>
    <span>Phone: 1300 958 471</span>
  </div>
</section>

</body>
</html>
```